Saint Wilfreda of mercy banners

In need of two banners designed.
Product Details:
Imprint Area:
Banner stands: 2-33.5"W x 79"H (full color),

Product Size:
Two Banner Stands: 34"W x 83"H including base,
See attached for specifics

* We would like the logo and "Annual Fundraiser" added above the logo or on either side of the logo.
* The problem we were running in to was that "Annual" and "Fundraiser" are not equal in length.

Banner Stand
* This will talk about what the foundation is
Logo with "Annual Fundraiser" incorporated
*You can also visit our website www.swmparishbellhaven.org and go to the Education Foundation page for more info
Q: Who benefits from the foundation?
A: All Saint Wilfreda of Mercy(SWM) parishioners and local people looking to enhance their faith.
Q: What does the foundation fund?
A: All learning opportunities provided by the parish
*KESTREL and Adult Bible Studies
*Faith Formation (Nursery-12 th Grade)
*RCIA and Sacramental Prep
*Books and CD's distributed during Lent and Advent
*SWM Elementary and Middle School and Vacation Bible School
*Parish Library and Mission

Banner(Horizontal)
* This is going to talk about our needs. I'm thinking on the top we could write something like:
Q: How can I help?
A: Donate your time, talent, and treasure

* Then we have 2 ways they can help: Volunteer and Donate
VOLUNTEER
Time: Can you help plan before, during, or after the event?
Talent: Do you have a special talent that might help us plan?
creative: help with decor or ideas
tech savy: help with social media and website, putting together slideshow
marketing: help get the word out
sales and outgoing personality: help solicit donations
DONATE
Talent: Do you have a special talent that you may be able to use to make an auction item? Could you knit a blanket, create a piece of art, offer a service like personal training or a hair cut? Are you the hostess with the mostest and would like to donate a party for someone?
Treasure: Do you own a business that could donate services or goods? Do you have a vacation home you would be willing to rent out? Would you be willing to donate money towards the planning or to the foundation?

*If there is room across the bottom we could put "Food * Drinks * Band * Silent/Live Auction"

Target Market(s)

Parishioners of Church

Industry/Entity Type

Non Profit

Font styles to use
Serif
Sans Serif

Colors
3276b5
0455a3

Requirements
Must have
• * Generic enough to be used year after year
• * Easy to read and not to overwhelming
Nice to have
• I would love to see some graphics included. You can add to my choosen colors if you think colorful is better

```html
<!DOCTYPE html>
<html lang="en">
<head>
<meta charset="utf-8">
<title>Saint Wilfreda of Mercy – Annual Fundraiser Banner</title>
<link rel="stylesheet" href="https://fonts.googleapis.com/css2?family=Raleway:ital,wght@0,500;0,700;0,800;0,900;1,500&display=swap">
<style>
  :root {
    --canvas: #ececec;
    --navy: #1f2a78;
    --navy-light: #33449e;
    --green: #9cc63b;
    --green-dark: #7fa82c;
    --yellow: #f7c424;
    --orange: #f07b1b;
    --purple: #ad4ea5;
    --sky: #2ea6df;
    --ink: #111111;
    --panel: #eef0f3;
    --white: #ffffff;
  }
  * { box-sizing: border-box; margin: 0; padding: 0; }
  html, body {
    width: 1125px; height: 1200px; overflow: hidden;
    background: var(--canvas);
    font-family: "Raleway", Arial, sans-serif;
  }
  .banner {
    position: absolute; left: 322px; top: 34px;
    width: 480px; height: 1132px; overflow: hidden;
    background: radial-gradient(ellipse at 50% 55%, #ffffff 0%, var(--panel) 60%, #dfe2e7 100%);
  }
  .banner-shapes { position: absolute; inset: 0; }
  .abs { position: absolute; }

  .org-name {
    left: 22px; top: 96px; width: 170px;
    color: var(--white); font-weight: 700; font-size: 19px; line-height: 1.2;
  }
  .event-title {
    left: 200px; top: 96px; width: 262px; text-align: center;
    color: var(--white); font-weight: 800; line-height: 1;
  }
  .event-title .line-1 { display: block; font-size: 52px; letter-spacing: 0.5px; }
  .event-title .line-2 { display: block; font-size: 31px; margin-top: 4px; letter-spacing: 0.3px; }

  .question { left: 22px; top: 276px; font-size: 20px; font-weight: 700; color: var(--navy); }
  .answer {
    left: 128px; top: 352px; width: 340px; text-align: center;
    font-size: 19px; font-weight: 800; line-height: 1.15; color: var(--navy);
  }

  .volunteer { left: 0; top: 452px; width: 480px; text-align: center; }
  .section-title { font-weight: 900; font-size: 26px; color: var(--orange); letter-spacing: 0.5px; }
  .volunteer .prompt-head { font-weight: 900; font-size: 20px; color: var(--ink); margin-top: 8px; }
  .volunteer .prompt { font-weight: 700; font-size: 13px; color: var(--ink); margin-top: 2px; }

  .skills { left: 0; top: 592px; width: 480px; }
  .skill { position: absolute; width: 120px; margin-left: -60px; text-align: center; }
  .skill svg { display: block; margin: 0 auto; }
  .skill-name { font-weight: 900; font-size: 12px; line-height: 1.1; color: var(--ink); margin-top: 24px; text-transform: uppercase; }
  .skill-note { font-style: italic; font-weight: 500; font-size: 9.5px; line-height: 1.2; color: #333; margin-top: 2px; }

  .donate-title { left: 34px; top: 762px; font-weight: 900; font-size: 28px; color: var(--ink); }

  .donate-item { left: 36px; width: 430px; }
  .donate-item .bar { position: absolute; left: 0; top: 0; width: 37px; }
  .donate-item .body { margin-left: 53px; }
  .donate-item h3 { font-weight: 900; font-size: 20px; line-height: 1; margin-bottom: 6px; }
  .donate-item p { font-weight: 700; font-size: 14.6px; line-height: 18px; color: var(--ink); }
  .item-talent { top: 806px; }
  .item-talent .bar { height: 126px; background: var(--purple); }
  .item-talent h3 { color: var(--purple); }
  .item-treasure { top: 950px; }
  .item-treasure .bar { height: 72px; background: var(--yellow); }
  .item-treasure h3 { color: var(--orange); }
  .bar svg { display: block; margin: 8px auto 0; }
</style>
</head>
<body>
<main class="banner">
  <svg class="banner-shapes" width="480" height="1132" viewBox="0 0 480 1132" aria-hidden="true">
    <defs>
      <linearGradient id="navyFade" x1="0" y1="0" x2="0" y2="1">
        <stop offset="0" stop-color="#1b2570"/>
        <stop offset="0.6" stop-color="#2a3a92"/>
        <stop offset="1" stop-color="#1f2a78"/>
      </linearGradient>
    </defs>
    <path d="M0 0 H480 V332 Q300 312 160 340 Q80 356 0 350 Z" fill="url(#navyFade)"/>
    <polygon points="0,42 480,22 480,194 0,210" fill="var(--green)"/>
    <polygon points="0,258 366,250 372,322 0,332" fill="var(--yellow)"/>
    <polygon points="118,330 205,328 208,348 122,350" fill="var(--green-dark)"/>
    <polygon points="112,344 480,336 480,414 118,420" fill="var(--green)"/>
  </svg>

  <div class="abs org-name">Saint Wilfreda<br>of Mercy</div>
  <h1 class="abs event-title"><span class="line-1">ANNUAL</span><span class="line-2">FUNDRAISER</span></h1>

  <p class="abs question">Q: HOW CAN I HELP?</p>
  <p class="abs answer">A: DONATE YOUR TIME,<br>TALENT, AND TREASURE</p>

  <section class="abs volunteer">
    <h2 class="section-title">VOLUNTEER</h2>
    <p class="prompt-head">TIME:</p>
    <p class="prompt">Can you help plan before, during, or after the event?</p>
    <p class="prompt-head">TALENT:</p>
    <p class="prompt">Do you have a special talent that might help us plan?</p>
  </section>

  <div class="abs skills">
    <div class="skill" style="left:71px">
      <svg width="60" height="60" viewBox="0 0 60 60" aria-hidden="true">
        <circle cx="30" cy="30" r="29" fill="var(--sky)"/>
        <path d="M40 16 L44 20 L30 34 L26 30 Z" fill="#fff"/>
        <path d="M25 32 L28 35 Q26 42 18 43 Q20 36 25 32 Z" fill="#fff"/>
      </svg>
      <p class="skill-name">Creative:</p>
      <p class="skill-note">help with decor<br>or ideas</p>
    </div>
    <div class="skill" style="left:185px">
      <svg width="60" height="60" viewBox="0 0 60 60" aria-hidden="true">
        <circle cx="30" cy="30" r="29" fill="var(--purple)"/>
        <rect x="17" y="18" width="26" height="18" rx="2" fill="none" stroke="#fff" stroke-width="2.5"/>
        <rect x="27" y="36" width="6" height="5" fill="#fff"/>
        <rect x="22" y="41" width="16" height="2.5" fill="#fff"/>
      </svg>
      <p class="skill-name">Tech Savy:</p>
      <p class="skill-note">help with social media<br>and website, putting<br>together slideshow</p>
    </div>
    <div class="skill" style="left:302px">
      <svg width="60" height="60" viewBox="0 0 60 60" aria-hidden="true">
        <circle cx="30" cy="30" r="29" fill="var(--green)"/>
        <path d="M18 26 H24 L38 18 V42 L24 34 H18 Z" fill="#fff"/>
        <path d="M22 34 L25 43 H29 L27 34 Z" fill="#fff"/>
        <path d="M41 25 Q45 30 41 35" fill="none" stroke="#fff" stroke-width="2.2"/>
      </svg>
      <p class="skill-name">Marketing:</p>
      <p class="skill-note">help get the<br>word out</p>
    </div>
    <div class="skill" style="left:425px">
      <svg width="60" height="60" viewBox="0 0 60 60" aria-hidden="true">
        <circle cx="30" cy="30" r="29" fill="var(--navy)"/>
        <circle cx="22" cy="22" r="4" fill="#fff"/>
        <circle cx="38" cy="22" r="4" fill="#fff"/>
        <circle cx="30" cy="30" r="4" fill="#fff"/>
        <path d="M16 36 Q16 28 22 28 Q27 28 27 33" fill="none" stroke="#fff" stroke-width="2.5"/>
        <path d="M44 36 Q44 28 38 28 Q33 28 33 33" fill="none" stroke="#fff" stroke-width="2.5"/>
        <path d="M23 44 Q23 36 30 36 Q37 36 37 44 Z" fill="#fff"/>
      </svg>
      <p class="skill-name">Sales and<br>Outgoing<br>Personality:</p>
      <p class="skill-note">help solicit donations</p>
    </div>
  </div>

  <h2 class="abs donate-title">DONATE</h2>

  <section class="abs donate-item item-talent">
    <div class="bar">
      <svg width="20" height="20" viewBox="0 0 20 20" aria-hidden="true">
        <circle cx="8" cy="7" r="4" fill="#fff"/>
        <path d="M1 19 Q1 12 8 12 Q15 12 15 19 Z" fill="#fff"/>
        <path d="M16 1 L17 4 L20 4 L17.5 6 L18.5 9 L16 7 L13.5 9 L14.5 6 L12 4 L15 4 Z" fill="#fff"/>
      </svg>
    </div>
    <div class="body">
      <h3>TALENT:</h3>
      <p>Do you have a special talent that you may be able to use to make an auction item? Could you knit a blanket, create a piece of art, offer a service like personal training or a hair cut? Are you the hostess with the mostest and would like to donate a party for someone?</p>
    </div>
  </section>

  <section class="abs donate-item item-treasure">
    <div class="bar">
      <svg width="20" height="20" viewBox="0 0 20 20" aria-hidden="true">
        <rect x="1.5" y="4" width="17" height="13" fill="none" stroke="#fff" stroke-width="2"/>
        <rect x="1.5" y="4" width="17" height="5" fill="#fff"/>
        <rect x="8" y="7" width="4" height="5" fill="var(--yellow)" stroke="#fff" stroke-width="1.5"/>
      </svg>
    </div>
    <div class="body">
      <h3>TREASURE:</h3>
      <p>Do you own a business that could donate services or goods? Do you have a vacation home you would be willing to rent out? Would you be willing to donate money towards the planning or to the foundation?</p>
    </div>
  </section>
</main>
</body>
</html>
```